Marks of Dunmore business card design

I need a clean, professional looking design using the attached logo with a bright green/ gray/dark gray/black colors. Maybe even an orange accent if it looks good. I am open to slight changes in the logo if needed. Details below on the info on what should be on the cards. We are a sign company in Ft. Lauderdale FL that specializes in yacht lettering on multi million dollar yachts.

Target Market(s)

marine industry, yachts

Industry/Entity Type

Business

Colors
9bcb3c
000000
606060
f37122

Requirements
Must have
• address: 4837 W. Tallow Rd.
• Coral Haven, FL 33412
• Phone: 954-518-4062
• email/website: marksofdunmore@postvane.com MarksofDunmore.com
Nice to have
• I would like it very clean and simple but professional looking. Nice layout and would prefer a darker background. Orange highlight only if it works.
Should not have
• Nothing fancy.

```html
<!DOCTYPE html>
<html lang="en">
<head>
<meta charset="utf-8">
<title>Marks of Dunmore – Business Card</title>
<link rel="stylesheet" href="https://fonts.googleapis.com/css2?family=Open+Sans:wght@400;600;800&display=swap">
<style>
  :root {
    --page-bg: #e9e6e1;
    --orange-light: #f39a32;
    --orange-mid: #ec8a26;
    --orange-deep: #d9661c;
    --card-black: #000000;
    --text-white: #ffffff;
    --text-dark: #1a1a1a;
  }
  * { margin: 0; padding: 0; box-sizing: border-box; }
  html, body {
    width: 1200px;
    height: 780px;
    overflow: hidden;
    background: var(--page-bg);
    font-family: "Open Sans", Arial, sans-serif;
  }
  .canvas {
    position: relative;
    width: 1200px;
    height: 780px;
    display: flex;
    align-items: center;
    justify-content: center;
  }
  .card {
    position: relative;
    width: 1000px;
    height: 572px;
    overflow: hidden;
    border-radius: 4px;
    background: linear-gradient(115deg, var(--orange-deep) 0%, var(--orange-mid) 45%, var(--orange-light) 100%);
    box-shadow: 0 10px 30px rgba(0,0,0,0.25);
  }
  .card__panel {
    position: absolute;
    inset: 0;
    width: 100%;
    height: 100%;
  }
  .card__panel path { fill: var(--card-black); }
  .brand-name {
    position: absolute;
    left: 250px;
    top: 70px;
    color: var(--orange-light);
    font-weight: 800;
    font-size: 60px;
    letter-spacing: 0.5px;
    line-height: 1;
  }
  .contact {
    position: absolute;
    left: 190px;
    top: 300px;
    color: var(--text-white);
  }
  .contact__name {
    font-weight: 600;
    font-size: 30px;
    line-height: 1.1;
  }
  .contact__role {
    color: var(--orange-light);
    font-size: 22px;
    line-height: 1.1;
    margin-bottom: 26px;
  }
  .contact__line {
    font-size: 22px;
    line-height: 1.35;
  }
  .contact__list {
    list-style: none;
    margin-top: 18px;
  }
  .contact__item {
    display: flex;
    align-items: center;
    gap: 10px;
    font-size: 22px;
    line-height: 1.4;
  }
  .contact__icon { width: 22px; height: 22px; flex: none; }
  .website {
    position: absolute;
    right: 36px;
    bottom: 28px;
    color: var(--text-dark);
    font-size: 20px;
  }
</style>
</head>
<body>
<main class="canvas">
  <section class="card" aria-label="Marks of Dunmore business card">
    <svg class="card__panel" viewBox="0 0 1000 572" preserveAspectRatio="none" aria-hidden="true">
      <path d="M215 0 H830 C930 170 880 400 620 572 H150 C70 400 95 160 215 0 Z"/>
    </svg>

    <h1 class="brand-name">Marks of Dunmore</h1>

    <div class="contact">
      <p class="contact__name">Evan Hollis</p>
      <p class="contact__role">Founder</p>
      <p class="contact__line">4837 W. Tallow Rd.</p>
      <p class="contact__line">Coral Haven, FL 33412</p>
      <ul class="contact__list">
        <li class="contact__item">
          <svg class="contact__icon" viewBox="0 0 22 22" aria-hidden="true">
            <circle cx="11" cy="11" r="10" fill="none" stroke="#f39a32" stroke-width="1.6"/>
            <path d="M7 8 Q7 6 9 6 L10 8 L9 9 Q10 12 13 13 L14 12 L16 13 Q16 15 14 15 Q8 14 7 8 Z" fill="#f39a32"/>
          </svg>
          954-518-4062
        </li>
        <li class="contact__item">
          <svg class="contact__icon" viewBox="0 0 22 22" aria-hidden="true">
            <circle cx="11" cy="11" r="10" fill="none" stroke="#f39a32" stroke-width="1.6"/>
            <rect x="6" y="7.5" width="10" height="7" fill="none" stroke="#f39a32" stroke-width="1.4"/>
            <path d="M6 7.5 L11 11.5 L16 7.5" fill="none" stroke="#f39a32" stroke-width="1.4"/>
          </svg>
          marksofdunmore@postvane.com
        </li>
      </ul>
    </div>

    <p class="website">MarksofDunmore.com</p>
  </section>
</main>
</body>
</html>
```